Save the Date for 77th birthday fundraiser

We need a design for a Save the Date as we are preparing to celebrate our founder Dale Penwarden’s 77 birthday next year.
We would like a professional illustrated Save the Date with the theme “How it started, How it’s going”. Attached is a picture from the early 70’s and another one from yesterday. We want him to look his absolute best.
We need the date, location, and contact details to RSVP incorporated into the design:
April 9
Milford Avery House, Austin Texas
team@guidebrightpath.com
AND PLEASE REMEMBER THIS IS A SURPRISE!
We would also like to include elements that evoke what he does: Author (he’s published 2 books), Speaker (a microphone), Business Coach, and Entrepreneur.
Feelings we would like to evoke when people see the image: Would like people to think we are a professional company that is throwing a fun event for all the clients and friends Dale has made along his extraordinary 50-year career.
Thank you so much!

```html
<!DOCTYPE html>
<html lang="en">
<head>
<meta charset="utf-8">
<title>Save the Date – Dale Penwarden's 77th Birthday</title>
<link rel="stylesheet" href="https://fonts.googleapis.com/css2?family=Cinzel:wght@400;600&family=Great+Vibes&family=Cormorant+Garamond:ital,wght@1,500&display=swap">
<style>
  :root {
    --royal-blue: #1c2a95;
    --deep-blue: #141f78;
    --glow-blue: #3147c4;
    --gold: #e6b94a;
    --gold-soft: #f0cd72;
    --white: #ffffff;
    --photo-warm: #b9a488;
    --photo-cool: #c8b8a6;
  }
  * { margin: 0; padding: 0; box-sizing: border-box; }
  html, body { width: 804px; height: 1200px; overflow: hidden; background: var(--deep-blue); }
  .invitation {
    position: relative;
    width: 804px;
    height: 1200px;
    overflow: hidden;
    background:
      radial-gradient(circle at 22% 18%, var(--glow-blue) 0, transparent 260px),
      radial-gradient(circle at 80% 55%, var(--glow-blue) 0, transparent 300px),
      radial-gradient(circle at 30% 85%, #2a3db5 0, transparent 240px),
      var(--royal-blue);
    font-family: "Cinzel", "Times New Roman", serif;
    color: var(--white);
    text-align: center;
  }
  .frame {
    position: absolute;
    inset: 32px;
    border: 2px solid var(--gold);
  }
  .brand {
    position: absolute;
    top: 72px;
    left: 0;
    right: 0;
    font-family: "Cinzel", "Times New Roman", serif;
    font-weight: 400;
    color: var(--white);
  }
  .brand-name { font-size: 42px; letter-spacing: 2px; line-height: 1.1; }
  .brand-tagline { font-size: 17px; letter-spacing: 5px; margin-top: 6px; }

  .era {
    position: absolute;
    top: 246px;
    width: 262px;
  }
  .era--started { left: 104px; }
  .era--going { left: 396px; }
  .era-label {
    font-size: 21px;
    color: var(--gold);
    letter-spacing: 1px;
    margin-bottom: 12px;
    line-height: 1;
  }
  .era-photo {
    width: 262px;
    height: 278px;
    border: 3px solid var(--white);
  }
  .era--started .era-photo { background: linear-gradient(160deg, #e2ddd6, #8f8880 70%, #5c5650); }
  .era--going .era-photo { background: linear-gradient(160deg, #d9c9b6, var(--photo-warm) 55%, #7a2a2a); }

  .save-the-date {
    position: absolute;
    top: 574px;
    left: 0; right: 0;
    font-family: "Great Vibes", "Brush Script MT", cursive;
    font-size: 104px;
    color: var(--gold-soft);
    line-height: 1;
  }
  .occasion {
    position: absolute;
    top: 690px;
    left: 0; right: 0;
    font-size: 23px;
    letter-spacing: 1.5px;
    line-height: 1.45;
  }
  .occasion sup { font-size: 13px; }

  .event-date {
    position: absolute;
    top: 806px;
    left: 0; right: 0;
    display: flex;
    justify-content: center;
    align-items: center;
    color: var(--gold);
    font-size: 40px;
    line-height: 1;
  }
  .event-date span { padding: 0 22px; }
  .event-date .divider { width: 2px; height: 66px; background: var(--gold); }

  .venue {
    position: absolute;
    top: 908px;
    left: 0; right: 0;
    font-size: 24px;
    letter-spacing: 1px;
  }
  .rsvp {
    position: absolute;
    top: 980px;
    left: 0; right: 0;
    font-family: "Cormorant Garamond", Georgia, serif;
    font-style: italic;
    font-weight: 500;
    font-size: 25px;
    color: var(--gold-soft);
  }
  .dots {
    position: absolute;
    top: 1044px;
    left: 0; right: 0;
    display: flex;
    justify-content: center;
    gap: 50px;
  }
  .dots i { width: 10px; height: 10px; border-radius: 50%; background: var(--gold); display: block; }
  .reminder {
    position: absolute;
    top: 1078px;
    left: 0; right: 0;
    font-size: 20px;
    line-height: 1.4;
    letter-spacing: 1px;
  }
  .career-emblem {
    position: absolute;
    left: 14px;
    bottom: 12px;
    width: 110px;
    height: 122px;
    background: linear-gradient(180deg, rgba(255,255,255,0.35), rgba(255,255,255,0.15));
    border-radius: 8px;
  }
</style>
</head>
<body>
<main class="invitation">
  <div class="frame"></div>

  <header class="brand">
    <div class="brand-name">Dale Penwarden</div>
    <div class="brand-tagline">GUIDE BRIGHT PATH</div>
  </header>

  <section class="era era--started">
    <h2 class="era-label">HOW IT STARTED</h2>
    <div class="era-photo" role="img" aria-label="Black and white portrait of Dale in the early 1970s, wearing a top hat and vest"></div>
  </section>
  <section class="era era--going">
    <h2 class="era-label">HOW IT'S GOING</h2>
    <div class="era-photo" role="img" aria-label="Recent portrait of Dale in a top hat and red vest"></div>
  </section>

  <h1 class="save-the-date">Save the Date</h1>

  <p class="occasion">TO CELEBRATE OUR FOUNDER<br>DALE PENWARDEN'S 77<sup>TH</sup> BIRTHDAY</p>

  <p class="event-date">
    <span>APRIL</span><i class="divider"></i><span>9</span><i class="divider"></i><span>2022</span>
  </p>

  <p class="venue">MILFORD AVERY HOUSE, AUSTIN TEXAS</p>

  <p class="rsvp">team@guidebrightpath.com</p>

  <div class="dots"><i></i><i></i><i></i><i></i><i></i></div>

  <p class="reminder">AND PLEASE REMEMBER<br>THIS IS A SURPRISE!</p>

  <div class="career-emblem" role="img" aria-label="Line illustration of a microphone standing on a stack of books"></div>
</main>
</body>
</html>
```